Wix Web design for a Residential redevelopment company

I need a website with a modern and elegant feel that will attract investors. I would like for the color scale to include the colors in our logo and also shades of grey for a modern feel. I need a page for property case studies in which each case study includes property before and after photos, an imbeded youtube video and text in the format of a math problem showing the amount the property was bought for -(minus) what the investor got in return -(minus) rehab costs -(minus) taxes and fees =(equals) Net Profit
However instead of there being an equal sign, I want the math problem to go vertically down with an underline for the equals sign.There needs to be an "About us," page, Investor Inquiries page, Contact Us Page, and Case studies page.
For font formatting, we like Corporate Gothic. Please make the website Wix friendly.

When someone clicks on one of the case study pictures, I would like the pictures to pull up in a click or swipe to the right manner similar to how pictures are structured on mebrank or pendosa.com

Target Market(s)

Investors

Industry/Entity Type

Real Estate

Number of Pages Required

5+ page

Font styles to use
Other font styles liked:
• Gothic Corporate

Requirements
Nice to have
• stock photos for the home page

```html
<!DOCTYPE html>
<html lang="en">
<head>
<meta charset="utf-8">
<title>Norvale Property Solutions</title>
<link href="https://fonts.googleapis.com/css2?family=Roboto:wght@400;500;700&family=Open+Sans:wght@400;600&display=swap" rel="stylesheet">
<style>
:root{
  --blue:#1763c4;
  --blue-deep:#0d4fa6;
  --green:#4ca51d;
  --green-light:#55b01f;
  --green-dark:#1d8b35;
  --footer:#1f8a30;
  --ink:#111;
  --grey:#555;
  --line:#c9c9c9;
  --white:#fff;
}
*{margin:0;padding:0;box-sizing:border-box}
html,body{width:1200px;height:3846px;overflow:hidden;background:#fff}
body{position:relative;font-family:'Roboto',Arial,sans-serif;color:var(--ink)}
.abs{position:absolute}
/* header */
.site-header{position:absolute;left:0;top:0;width:1200px;height:97px;background:#fff}
.brand{position:absolute;left:182px;top:18px;display:flex;align-items:center;gap:12px}
.brand-mark{width:58px;height:58px;background:var(--green-dark)}
.brand-name{font-family:'Roboto',sans-serif;font-weight:700;font-size:34px;color:var(--green-dark);line-height:1}
.nav a{position:absolute;top:40px;font-size:15px;font-weight:500;color:#222;text-decoration:none;white-space:nowrap}
.nav a.active{color:var(--green)}
/* hero */
.hero{position:absolute;left:0;top:97px;width:1200px;height:580px;background:linear-gradient(180deg,#3e6fb4 0%,#5a86c4 35%,#44505f 70%,#2b3a2f 100%)}
.call-btn{position:absolute;left:843px;top:100px;width:175px;height:36px;background:var(--green-dark);color:#fff;font-size:13px;display:flex;align-items:center;justify-content:center;gap:7px}
.hero-card{position:absolute;left:182px;top:415px;width:280px;height:349px;background:var(--blue);color:#fff;padding:36px 34px}
.hero-card h1{font-size:22px;font-weight:500;line-height:1.25}
.hero-card p{font-family:'Open Sans',sans-serif;font-size:11.5px;line-height:1.6;margin-top:16px}
.hero-card hr{border:0;border-top:1px solid #fff;margin:18px 0}
.hero-card .price{text-align:center;font-size:22px;font-weight:500}
.hero-card .more{display:block;margin:14px auto 0;width:172px;height:32px;border:2px solid #fff;font-size:12px;text-align:center;line-height:28px}
/* section headings */
.section-title{position:absolute;left:0;width:1200px;text-align:center;font-size:26px;font-weight:500;color:var(--ink)}
.section-title.blue{color:var(--blue-deep)}
/* listings */
.listing{position:absolute;top:877px;width:263px}
.listing .photo{height:280px}
.listing h3{margin-top:30px;font-size:17px;font-weight:500;color:var(--green)}
.stats{margin-top:14px;font-family:'Open Sans',sans-serif;font-size:13.5px;width:230px}
.stats div{display:flex;height:26px;align-items:center}
.stats span:first-child{width:180px}
.stats .net{color:var(--blue);font-weight:600}
.listing .click{display:block;margin-top:16px;width:138px;height:27px;border:2px solid var(--green);font-size:11px;text-align:center;line-height:23px}
/* top properties */
.band{position:absolute;left:0;width:1200px}
.band.light{top:1597px;height:380px;background:var(--green-light)}
.band.dark{top:1977px;height:374px;background:var(--green-dark)}
.feature-photo{position:absolute}
.feature{position:absolute;color:#fff;width:330px}
.feature h3{font-size:20px;font-weight:400}
.feature .stats{font-size:12.5px;margin-top:14px;width:240px}
.feature .stats div{height:25px}
.feature .stats span:first-child{width:175px}
.feature .stats .net{color:#fff;font-weight:700}
.feature p{font-family:'Open Sans',sans-serif;font-size:11px;line-height:1.5;margin-top:14px}
.feature .link{margin-top:10px;font-size:15px;font-weight:500}
/* why */
.why{position:absolute;top:2530px;width:260px;text-align:center}
.why h4{margin-top:22px;font-size:17px;font-weight:500;color:var(--blue);line-height:1.2}
.why p{margin-top:14px;font-family:'Open Sans',sans-serif;font-size:11.5px;line-height:1.55;color:var(--grey)}
/* testimonials */
.testimonials{position:absolute;left:0;top:2777px;width:1200px;height:418px;background:linear-gradient(135deg,#2d5fb0 0%,#1c4a9a 50%,#133a82 100%)}
.testimonials h2{position:absolute;left:0;top:62px;width:1200px;text-align:center;color:#fff;font-size:26px;font-weight:500}
.quote{position:absolute;top:150px;width:220px;text-align:center;color:#fff}
.quote .mark{font-size:46px;font-weight:700;line-height:40px;height:36px}
.quote p{font-family:'Open Sans',sans-serif;font-size:13px;line-height:1.45}
.quote .author{margin-top:26px;font-size:14px}
/* contact */
.label{position:absolute;font-size:14px;font-weight:500;color:var(--blue);line-height:1.4}
.body-text{position:absolute;font-family:'Open Sans',sans-serif;font-size:13.5px;line-height:1.6;color:#333}
.map{position:absolute;left:233px;top:3431px;width:331px;height:148px;background:linear-gradient(135deg,#e6e6e6,#cfcfcf)}
.field{position:absolute;left:659px;width:300px;height:29px;border:1px solid #999;font-family:'Open Sans',sans-serif;font-size:11px;color:#888;padding:6px 10px}
.send{position:absolute;left:895px;top:3615px;width:64px;height:29px;background:var(--blue-deep);color:#fff;font-size:13px;text-align:center;line-height:29px}
/* footer */
.site-footer{position:absolute;left:0;top:3785px;width:1200px;height:61px;background:var(--footer);color:#fff}
.site-footer .copy{position:absolute;left:226px;top:22px;font-size:12px}
.social{position:absolute;top:17px;width:27px;height:27px;border:1.5px solid #fff;border-radius:50%}
</style>
</head>
<body>

<header class="site-header">
  <div class="brand"><div class="brand-mark"></div><span class="brand-name">NORVALE</span></div>
  <nav class="nav">
    <a class="active" style="left:454px">HOME</a>
    <a style="left:528px">ABOUT US</a>
    <a style="left:631px">INVESTOR INQUIRIES</a>
    <a style="left:805px">CASE STUDIES</a>
    <a style="left:938px">CONTACT US</a>
  </nav>
</header>

<section class="hero" role="img" aria-label="Modern two-storey luxury house lit at dusk beside a pool"></section>
<div class="call-btn">
  <svg width="13" height="13" viewBox="0 0 24 24" fill="#fff"><path d="M6.6 10.8a15.1 15.1 0 0 0 6.6 6.6l2.2-2.2c.3-.3.7-.4 1-.2 1.1.4 2.3.6 3.6.6.6 0 1 .4 1 1V20c0 .6-.4 1-1 1C10.6 21 3 13.4 3 4c0-.6.4-1 1-1h3.5c.6 0 1 .4 1 1 0 1.3.2 2.5.6 3.6.1.3 0 .7-.2 1z"/></svg>
  Call us! 123-456-7890
</div>
<div class="hero-card">
  <h1>PROPERTY TITLE<br>METUS AUGUE<br>CONVALLIS</h1>
  <p>Fermentum vel congue id euismod in elit fusce ultricies orci ac feugiat suscipit leo massa sodales velit et scelerisque mi tortor at ipsum digula</p>
  <hr>
  <div class="price">$2,000,000</div>
  <span class="more">VIEW MORE</span>
</div>

<h2 class="section-title" style="top:806px">PROPERTIES LISTINGS</h2>

<article class="listing" style="left:192px">
  <div class="photo" role="img" aria-label="Grey suburban house with green lawn and path" style="background:linear-gradient(180deg,#8fb3d9,#6f7b86 55%,#5c9a33)"></div>
  <h3>PROPERTY TITLE HERE</h3>
  <div class="stats"><div><span>Property Rate:</span><span>$58255</span></div><div><span>Return on investment:</span><span>-$2522</span></div><div><span>Rehab cost:</span><span>-$1152</span></div><div><span>Taxes &amp; fees:</span><span>-$2950</span></div><div class="net"><span>Net Profit</span><span>$51631</span></div></div>
  <span class="click">CLICK HERE</span>
</article>
<article class="listing" style="left:477px">
  <div class="photo" role="img" aria-label="Stone-fronted house at sunset with driveway" style="background:linear-gradient(180deg,#d8a0a8,#6d6a73 50%,#3b3a3f)"></div>
  <h3>PROPERTY TITLE HERE</h3>
  <div class="stats"><div><span>Property Rate:</span><span>$58255</span></div><div><span>Return on investment:</span><span>-$2522</span></div><div><span>Rehab cost:</span><span>-$1152</span></div><div><span>Taxes &amp; fees:</span><span>-$2950</span></div><div class="net"><span>Net Profit</span><span>$51631</span></div></div>
  <span class="click">CLICK HERE</span>
</article>
<article class="listing" style="left:759px">
  <div class="photo" role="img" aria-label="White modern house with hedges" style="background:linear-gradient(180deg,#d9e2ea,#c8c8c6 55%,#7a8a6a)"></div>
  <h3>PROPERTY TITLE HERE</h3>
  <div class="stats"><div><span>Property Rate:</span><span>$58255</span></div><div><span>Return on investment:</span><span>-$2522</span></div><div><span>Rehab cost:</span><span>-$1152</span></div><div><span>Taxes &amp; fees:</span><span>-$2950</span></div><div class="net"><span>Net Profit</span><span>$51631</span></div></div>
  <span class="click">CLICK HERE</span>
</article>

<h2 class="section-title" style="top:1447px">TOP PROPERTIES</h2>

<div class="band light"></div>
<div class="band dark"></div>
<div class="feature-photo" role="img" aria-label="Blue-grey two-storey home with lawn at dusk" style="left:233px;top:1541px;width:303px;height:336px;background:linear-gradient(180deg,#8aa4c4,#55627a 55%,#3f6b2a)"></div>
<div class="feature" style="left:600px;top:1642px">
  <h3>PROPERTY TITLE HERE</h3>
  <div class="stats"><div><span>Property Rate:</span><span>$58255</span></div><div><span>Return on investment:</span><span>-$2522</span></div><div><span>Rehab cost:</span><span>-$1152</span></div><div><span>Taxes &amp; fees:</span><span>-$2950</span></div><div class="net"><span>Net Profit</span><span>$51631</span></div></div>
  <p>Morbi ornare gravida elit integer congue augue et malesuada iaculis ipsum dui aliquet felis at cursus magna nisl nec</p>
  <div class="link">CLICK HERE</div>
</div>
<div class="feature" style="left:251px;top:2040px">
  <h3>PROPERTY TITLE HERE</h3>
  <div class="stats"><div><span>Property Rate:</span><span>$58255</span></div><div><span>Return on investment:</span><span>-$2522</span></div><div><span>Rehab cost:</span><span>-$1152</span></div><div><span>Taxes &amp; fees:</span><span>-$2950</span></div><div class="net"><span>Net Profit</span><span>$51631</span></div></div>
  <p>Morbi ornare gravida elit integer congue augue et malesuada iaculis ipsum dui aliquet felis at cursus magna nisl nec</p>
  <div class="link">CLICK HERE</div>
</div>
<div class="feature-photo" role="img" aria-label="Navy craftsman house with stone path among trees" style="left:662px;top:2044px;width:305px;height:333px;background:linear-gradient(180deg,#c7d3de,#3d4a66 50%,#4d7a30)"></div>

<h2 class="section-title blue" style="top:2447px">WHY CHOOSE US</h2>

<div class="why" style="left:203px">
  <svg width="40" height="48" viewBox="0 0 24 28"><text x="12" y="24" text-anchor="middle" font-family="Roboto,sans-serif" font-size="28" font-weight="700" fill="#4ca51d">$</text></svg>
  <h4>FREE REGISTRATION<br>NO EXTRA COST</h4>
  <p>Morbi ornare gravida elit integer congue augue et malesuada iaculis ipsum dui aliquet felis at cursus magna nis</p>
</div>
<div class="why" style="left:467px">
  <svg width="44" height="48" viewBox="0 0 24 24"><path fill="#4ca51d" d="M22.7 19l-9.1-9.1c.9-2.3.4-5-1.5-6.9-2-2-5-2.4-7.4-1.3L9 6 6 9 1.6 4.7C.4 7.1.9 10.1 2.9 12.1c1.9 1.9 4.6 2.4 6.9 1.5l9.1 9.1c.4.4 1 .4 1.4 0l2.3-2.3c.5-.4.5-1.1.1-1.4z"/></svg>
  <h4>PROPERTY SERVICES<br>FREE OF CHARGE</h4>
  <p>Morbi ornare gravida elit integer congue augue et malesuada iaculis ipsum dui aliquet felis at cursus magna nis</p>
</div>
<div class="why" style="left:731px">
  <svg width="40" height="48" viewBox="0 0 24 24"><path fill="#4ca51d" d="M12 2C8.1 2 5 5.1 5 9c0 5.2 7 13 7 13s7-7.8 7-13c0-3.9-3.1-7-7-7zm0 9.5a2.5 2.5 0 1 1 0-5 2.5 2.5 0 0 1 0 5z"/></svg>
  <h4>LARGE COVERAGE<br>OFFICES IN 4 LOCATIONS</h4>
  <p>Morbi ornare gravida elit integer congue augue et malesuada iaculis ipsum dui aliquet felis at cursus magna nis</p>
</div>

<section class="testimonials" role="img" aria-label="Modern white house at dusk under a blue overlay">
  <h2>WHAT OUR CLIENTS THINK</h2>
  <div class="quote" style="left:210px"><div class="mark">&ldquo;</div><p>"Morbi ornare gravida elit Integer congue augue et malesuada iaculis ipsum dui aliquet felis at cursus magna nisl nec elit Praesent."</p><div class="author">By Author Name</div></div>
  <div class="quote" style="left:482px"><div class="mark">&ldquo;</div><p>"Morbi ornare gravida elit Integer congue augue et malesuada iaculis ipsum dui aliquet felis at cursus magna nisl nec elit Praesent."</p><div class="author">By Author Name</div></div>
  <div class="quote" style="left:754px"><div class="mark">&ldquo;</div><p>"Morbi ornare gravida elit Integer congue augue et malesuada iaculis ipsum dui aliquet felis at cursus magna nisl nec elit Praesent."</p><div class="author">By Author Name</div></div>
</section>

<h2 class="section-title blue" style="top:3272px">CONTACT US</h2>

<div class="label" style="left:233px;top:3340px">ADDRESS</div>
<div class="body-text" style="left:233px;top:3372px">410 Harlow Avenue<br>Brookfield, CA 94016</div>
<div class="map" role="img" aria-label="Street map of the office location"></div>
<div class="label" style="left:233px;top:3606px;font-size:12.5px">TO SPEAK WITH AN AGENT,<br>PLEASE CALL OR EMAIL US</div>
<div class="body-text" style="left:233px;top:3652px;font-size:12px;line-height:1.5">Email: info@norvaleps.com<br>Tel: 123-456-7890<br>Fax: 123-456-7890</div>

<div class="label" style="left:659px;top:3342px">ALTERNATIVELY YOU CAN FILL IN THE<br>FOLLOWING CONTACT FORM</div>
<div class="field" style="top:3419px">Name*</div>
<div class="field" style="top:3455px">Email*</div>
<div class="field" style="top:3491px">Subject</div>
<div class="field" style="top:3528px;height:75px">Message</div>
<div class="send">Send</div>

<footer class="site-footer">
  <div class="copy">© 2018 Company Name. All right reserved</div>
  <span class="social" style="left:915px"></span>
  <span class="social" style="left:949px"></span>
  <span class="social" style="left:983px"></span>
</footer>

</body>
</html>
```